IT Network Consultancy - Business Card

t4 linkways is a IT network consultancy based in London. We're looking for a smart, modern and professional business card design. Our website is here: www.t4linkways.co.uk

Key things that should be included on the card (with examples):

Company Logo
Name
Position / Job Title: Network Consultant
Mobile Phone Number: +44 (0) 7700 900418
Land Line: +44 (0) 1632 960274
Email Address: name@t4linkways.co.uk
Web Site URL: www.t4linkways.co.uk

Target Market(s)

Large enterprise / global companies / corporates

Industry/Entity Type

Business

Requirements
Must have
• Incorporate our logo - which is attached to the project. They are in AI format (can be opened in Inkscape).

The design should be double sided and fit on a UK standard 85mm × 55mm card and be in a format that retains the quality when printed.
Nice to have
• The project does not have to conform to the colour of our website but this should give you inspiration of the style we like.
Should not have
• Bright colours. Pictures are not necessary.

```html
<!DOCTYPE html>
<html lang="en">
<head>
<meta charset="utf-8">
<title>t4 linkways – Business Card</title>
<link rel="stylesheet" href="https://fonts.googleapis.com/css2?family=Questrial&family=Open+Sans:wght@600;700&display=swap">
<style>
  :root {
    --page: #ffffff;
    --slate-dark: #333d47;
    --slate-mid: #4a5662;
    --slate-light: #5e6c79;
    --paper: #ffffff;
    --paper-shade: #e9ecef;
    --brand-ink-front: #4b5661;
    --brand-ink-back: #d9dde1;
    --name-ink: #ffffff;
    --title-ink: #8e9aa4;
    --label-ink: #8e9aa4;
    --value-ink: #e8ebee;
    --sheen: rgba(255,255,255,0.55);
  }
  * { margin: 0; padding: 0; box-sizing: border-box; }
  html, body { width: 1200px; height: 900px; overflow: hidden; background: var(--page); }
  .canvas { position: relative; width: 1200px; height: 900px; }

  .card {
    position: absolute;
    top: 296px;
    width: 500px;
    height: 313px;
    overflow: hidden;
    box-shadow: 2px 3px 5px rgba(0,0,0,0.35);
  }
  .card--front { left: 84px; }
  .card--back { left: 619px; }

  /* Front */
  .front__head {
    position: absolute; left: 0; top: 0; width: 100%; height: 116px;
    background: radial-gradient(ellipse 70% 120% at 75% 0%, var(--paper) 40%, var(--paper-shade) 100%);
  }
  .front__body {
    position: absolute; left: 0; top: 116px; width: 100%; height: 165px;
    background: var(--slate-dark);
  }
  .front__foot {
    position: absolute; left: 0; top: 281px; width: 100%; height: 32px;
    background: linear-gradient(to bottom, #47525d, var(--slate-light) 60%);
  }
  .sheen-line {
    position: absolute; height: 1px;
    background: linear-gradient(to right, transparent, var(--sheen) 50%, transparent);
  }
  .front__head-line { left: 60px; right: 0; top: 115px; }
  .front__foot-line { left: 120px; right: 60px; top: 281px; }

  .brand {
    position: absolute;
    font-family: "Open Sans", sans-serif;
    font-weight: 600;
    white-space: nowrap;
  }
  .front .brand { left: 32px; top: 68px; font-size: 26px; color: var(--brand-ink-front); }

  .holder { position: absolute; right: 35px; top: 134px; text-align: right; font-family: "Open Sans", sans-serif; }
  .holder__name { font-size: 19px; font-weight: 700; color: var(--name-ink); line-height: 24px; }
  .holder__role { font-size: 12.5px; font-weight: 700; color: var(--title-ink); line-height: 16px; }

  .contacts { position: absolute; left: 40px; top: 192px; list-style: none; font-family: "Questrial", sans-serif; font-size: 14.5px; line-height: 18px; }
  .contacts li { display: flex; }
  .contacts__label { width: 20px; color: var(--label-ink); font-family: "Open Sans", sans-serif; font-weight: 700; font-size: 13px; }
  .contacts__value { color: var(--value-ink); }

  /* Back */
  .card--back {
    background: linear-gradient(to bottom, var(--slate-light) 0%, #4a5661 38%, #4a5661 62%, var(--slate-light) 100%);
  }
  .back__band {
    position: absolute; left: 0; top: 120px; width: 100%; height: 72px;
    background: var(--slate-dark);
  }
  .back__band-top { left: 0; right: 0; top: 120px; }
  .back__band-bottom { left: 0; right: 0; top: 191px; }
  .card--back .brand {
    left: 0; right: 0; top: 133px; text-align: center;
    font-size: 34px; color: var(--brand-ink-back);
  }
</style>
</head>
<body>
<div class="canvas">
  <section class="card card--front front" aria-label="Business card front">
    <div class="front__head"></div>
    <div class="sheen-line front__head-line"></div>
    <div class="front__body"></div>
    <div class="front__foot"></div>
    <div class="sheen-line front__foot-line"></div>

    <div class="brand">t4 linkways</div>

    <div class="holder">
      <p class="holder__name">Daniel Marsh</p>
      <p class="holder__role">Network Consultant</p>
    </div>

    <ul class="contacts">
      <li><span class="contacts__label">p.</span><span class="contacts__value">+44 (0) 1632 960274</span></li>
      <li><span class="contacts__label">m.</span><span class="contacts__value">+44 (0) 7700 900418</span></li>
      <li><span class="contacts__label">e.</span><span class="contacts__value">danielmarsh@t4linkways.co.uk</span></li>
      <li><span class="contacts__label">w.</span><span class="contacts__value">www.t4linkways.co.uk</span></li>
    </ul>
  </section>

  <section class="card card--back" aria-label="Business card back">
    <div class="back__band"></div>
    <div class="sheen-line back__band-top"></div>
    <div class="sheen-line back__band-bottom"></div>
    <div class="brand">t4 linkways</div>
  </section>
</div>
</body>
</html>
```